【依頼の目的/概要】
電子書籍(lumora)の表紙デザインをお願いします。

【画像サイズ】※RXMより抜粋
表紙ファイルの理想的な寸法は2,560×1,600ピクセルです。
注:画像の寸法は1,000×625ピクセル以上であることが必要です。
画像の最大の寸法は10,000×10,000ピクセルです。

【タイトル】
黄金のレシピ
-10歳!本当の美しさに出会える魔法

【サブタイトル】
あなたは幸せ顔?診断テストが満載!
症状別に冷え・食・香りで解決!

【著者】
美容経歴20年以上・小学生~80歳のお悩み解決5000人以上
トータル美容アドバイザー:森川ゆかり(ブルームリーフ代表)

【本の内容】
この本は食生活・隠れ冷えなどを改善し、精油の力で美容健康に
導く本です。
ご自分の今の状態が解り、それぞれの不調・悩みを改善する
診断テストが盛りだくさんです。
以下に本の目次を書き出しました。
原稿も添付ファイルしますので宜しくお願いします。

第1章|真の美しさを引き出す土台づくり
◆気・血・水のバランスを整える
◆気・血・水のタイプ別:特徴
◆気・血・水のタイプ別:改善策
◆木・火・土・金・水
五行説で心身の弱点を診断
◆五行の診断テスト
◆五行別:改善策

第2章|美肌になるための食べ物
◆腸内環境を整えるオススメ食品
◆美肌になる食べ物

第3章|隠れ冷えを改善して、免疫力UP
◆あなたの体の「冷え」はどのタイプ?
◆各タイプ別:改善策

第4章|今日から簡単に取り入れられる!
お悩み別!美容の裏ワザQ&A
◆Q1:かかとのガサガサ、どうにかしたい!
◆Q2:何だか最近、顔がくすんでみえます・・・
◆Q3:お顔のたるみ、年のせいだから仕方ない?
◆Q4:爪が割れやすくなってきました・・・
◆Q5:お肌の乾燥が気になります!
◆Q6:タルミに効果的なマッサージは?
◆Q7:冬の紫外線対策って必要ですか?
◆Q8:年々、白髪や薄毛が気になります・・・
◆Q9:マスカラをキレイに塗りたい!
◆Q10:眉を早くキレイに描きたい!
◆Q11:正しいクレンジング方法は?

第5章|香りのある暮らし
精油の活用法&最新情報
◆皮脳同根の原理で脳ストレスを減らそう
◆精油を買う時のポイント
◆好きな香りで作る芳香剤
◆更年期にオススメの精油活用法
◆吸収のメカニズム・香りの経路
◆レジリエンスを高める4つのレッスン
◆あなたにぴったりな香りはどれ?
◆知られざる精油の効果・効能

【デザイン要望】
表紙のイラストは添付しますので、そのイラストを
使ってください。(ミストの女性)

デザインはご自由な発想でお願いします。

文字はタイトル、サブタイトル、著者を入れてください。

次点・次々点の方への参加報酬を設定いたしました。
ご応募を楽しみにお待ちしております。
その他何かご不明な点がございましたら、お気軽にご質問下さい。
よろしくお願いいたします。

この度は素晴らしいデザインをして頂きありがとうございました。
一目でパッと目につき、タイトル文字もはっきりしていて優しい
色合いにとても惹かれました。
何度も修正して頂きありがとうございます。

皆様、この度は素晴らしい沢山のご提案をありがとうございました。
お一人お一人にお礼を申し上げることができませんが、この場をお借りして
お礼申し上げます。本当に皆様お忙しい中ありがとうございました。

```html
<!DOCTYPE html>
<html lang="ja">
<head>
<meta charset="utf-8">
<title>黄金のレシピ</title>
<link href="https://fonts.googleapis.com/css2?family=Shippori+Mincho+B1:wght@600;800&family=Zen+Maru+Gothic:wght@500;700;900&display=swap" rel="stylesheet">
<style>
  :root{
    --cream:#fffaf3;
    --pink:#f29cb6;
    --pink-deep:#e8638c;
    --yellow:#fbeb9e;
    --brown:#5b3a2c;
    --white:#ffffff;
  }
  *{margin:0;padding:0;box-sizing:border-box;}
  html,body{width:749px;height:1200px;overflow:hidden;background:var(--cream);}
  .cover{position:relative;width:749px;height:1200px;overflow:hidden;background:var(--cream);
    font-family:"Zen Maru Gothic",sans-serif;color:var(--brown);}
  .backdrop{position:absolute;inset:0;}
  .illustration{position:absolute;left:190px;top:240px;width:380px;height:690px;
    background:radial-gradient(ellipse at 55% 45%,#fde6ea 0%,#fff4f2 55%,rgba(255,250,243,0) 80%);}
  .title{position:absolute;left:14px;top:8px;font-family:"Shippori Mincho B1",serif;font-weight:800;color:var(--brown);line-height:1;}
  .title-main{font-size:168px;letter-spacing:-4px;display:flex;align-items:flex-end;}
  .title-no{display:inline-flex;width:58px;height:58px;border-radius:50%;background:var(--brown);color:var(--white);
    font-size:38px;align-items:center;justify-content:center;margin:0 0 18px 6px;}
  .title-sub{font-size:104px;letter-spacing:2px;margin:6px 0 0 6px;}
  .minus-badge{position:absolute;left:560px;top:-18px;width:190px;height:190px;border-radius:50%;background:var(--white);
    color:var(--pink-deep);text-align:center;font-weight:900;line-height:1;padding-top:44px;}
  .minus-badge .label{font-size:20px;letter-spacing:2px;}
  .minus-badge .num{font-size:80px;font-family:"Shippori Mincho B1",serif;}
  .minus-badge .unit{font-size:30px;}
  .tagline{position:absolute;right:14px;top:232px;writing-mode:vertical-rl;font-family:"Shippori Mincho B1",serif;
    font-weight:800;font-size:56px;line-height:1;letter-spacing:2px;color:var(--brown);white-space:nowrap;}
  .tagline .accent{color:var(--pink-deep);font-size:66px;}
  .question{position:absolute;left:24px;top:560px;writing-mode:vertical-rl;font-family:"Shippori Mincho B1",serif;
    font-weight:800;font-size:46px;letter-spacing:2px;line-height:1;color:var(--white);white-space:nowrap;}
  .remedy-lead{position:absolute;left:112px;top:905px;font-size:28px;font-weight:700;white-space:nowrap;}
  .remedy-venn{position:absolute;left:108px;top:944px;}
  .remedy-tail{position:absolute;left:292px;top:1064px;font-size:32px;font-weight:900;white-space:nowrap;}
  .test-pill{position:absolute;left:40px;top:1128px;padding:6px 26px;border:3px solid var(--pink-deep);border-radius:30px;
    background:var(--white);color:var(--pink-deep);font-size:32px;font-weight:900;white-space:nowrap;}
  .career-badge{position:absolute;left:474px;top:808px;width:176px;height:176px;border-radius:50%;background:var(--pink-deep);
    color:var(--white);text-align:center;line-height:1.2;padding-top:32px;font-weight:700;font-size:18px;}
  .career-badge .big{font-size:28px;font-weight:900;}
  .career-badge .small{font-size:16px;margin-top:4px;}
  .author{position:absolute;left:446px;top:1032px;width:290px;text-align:center;white-space:nowrap;}
  .author-role{font-size:20px;font-weight:700;}
  .author-name{font-family:"Shippori Mincho B1",serif;font-weight:800;font-size:54px;line-height:1.15;letter-spacing:2px;}
  .author-org{font-size:20px;font-weight:700;}
</style>
</head>
<body>
<div class="cover">
  <svg class="backdrop" width="749" height="1200" viewBox="0 0 749 1200" aria-hidden="true">
    <polygon points="520,0 749,0 749,250" fill="var(--pink)"/>
    <polygon points="749,180 749,1200 600,1200 560,900 575,230" fill="var(--yellow)"/>
    <polygon points="0,430 180,560 200,980 0,1040" fill="var(--pink)"/>
    <polygon points="0,1040 200,980 430,880 430,1200 0,1200" fill="var(--yellow)"/>
    <polygon points="430,980 749,1020 749,1200 430,1200" fill="var(--cream)"/>
  </svg>

  <div class="illustration" role="img" aria-label="ミストを吹きかける女性のイラストと舞う花びら"></div>

  <h1 class="title">
    <div class="title-main">黄金<span class="title-no">の</span></div>
    <div class="title-sub">レシピ</div>
  </h1>

  <div class="minus-badge">
    <div class="label">マイナス</div>
    <div class="num">-10</div>
    <div class="unit">歳!</div>
  </div>

  <p class="tagline">本当の<span class="accent">美</span>しさに出会える<span class="accent">魔法</span></p>

  <p class="question">あなたは幸せ顔?</p>

  <div class="remedy-lead">症状別に</div>
  <svg class="remedy-venn" width="180" height="170" viewBox="0 0 180 170">
    <g fill="rgba(255,255,255,0.85)" stroke="var(--pink-deep)" stroke-width="3">
      <circle cx="90" cy="50" r="46"/>
      <circle cx="52" cy="118" r="46"/>
      <circle cx="128" cy="118" r="46"/>
    </g>
    <g fill="var(--pink-deep)" font-family="Zen Maru Gothic, sans-serif" font-weight="900" text-anchor="middle">
      <text x="90" y="56" font-size="28">冷え</text>
      <text x="46" y="130" font-size="32">食</text>
      <text x="134" y="128" font-size="28">香り</text>
    </g>
  </svg>
  <div class="remedy-tail">で解決!</div>

  <div class="test-pill">診断テストが満載!</div>

  <div class="career-badge">
    <div>美容経歴</div>
    <div class="big">20年以上</div>
    <div class="small">小学生~80歳の<br>お悩み解決<br>5000人以上</div>
  </div>

  <div class="author">
    <div class="author-role">トータル美容アドバイザー</div>
    <div class="author-name">森川ゆかり</div>
    <div class="author-org">(ブルームリーフ代表)</div>
  </div>
</div>
</body>
</html>
```